Hip / Cool Business Card for Custom Accessory Company

I would like to get a 2 sided design for standard size business cards, glossy (2 inches x 3.5 inches). Can be landscape or portrait layout! The design should include our logo (attached). The card should be extremely clear that the company is Tin Lantern. Should also have our URL clear. Should also use the color scheme seen on our upcoming site, tinlantern-example.com. The font we use is called "hurry up." Other than that, please go-to-town. We are targeting 15-45 y.o. market, with a skew on the 20-30 crowd. We do custom and stock iPhone cases as well as Cufflinks, Winestoppers; see the website for more.
Updates

Project Deadline Extended
Reason: Extending in case the US July 4th Holiday is keeping people from working!!

Industry/Entity Type

Landscape

Requirements
Must have
• Must be clear that the website is tinlantern-example.com. Must be clear that custom designs are an option.
Nice to have
• images of our designs. examples of our designs.
Should not have
• hard on the eyes contrasting colors such as orange on black. green on blue. Should not have any fonts that are considered "old" like Times New Roman. But decorative fonts are fine.

```html
<!DOCTYPE html>
<html lang="en">
<head>
<meta charset="utf-8">
<title>Tin Lantern – Business Card</title>
<link rel="stylesheet" href="https://fonts.googleapis.com/css2?family=Open+Sans:wght@400;700&display=swap">
<style>
  :root {
    --backdrop: #e6e7e9;
    --card-white: #ffffff;
    --brand-blue: #0a63b5;
    --accent-sky: #9fd3f5;
    --mark-teal: #2a9ea6;
    --mark-grey: #dcdcdc;
    --ink: #1c1c1c;
    --on-blue: #ffffff;
  }
  * { box-sizing: border-box; margin: 0; padding: 0; }
  html, body {
    width: 1200px; height: 900px; overflow: hidden;
    background: var(--backdrop);
    font-family: "Open Sans", Arial, sans-serif;
  }
  .sheet { position: relative; width: 1200px; height: 900px; }
  .card {
    position: absolute; left: 250px; width: 700px; height: 400px;
    overflow: hidden; box-shadow: 0 6px 18px rgba(0,0,0,.18);
  }
  .card--back { top: 40px; background: var(--brand-blue); }
  .card--front { top: 460px; background: var(--card-white); }

  /* back side */
  .back-brand {
    position: absolute; left: 0; right: 0; top: 95px;
    display: flex; align-items: center; justify-content: center; gap: 18px;
  }
  .back-brand__dot { width: 76px; height: 76px; border-radius: 50%; background: var(--mark-grey); }
  .back-brand__name { color: var(--on-blue); font-weight: 700; font-size: 40px; }
  .back-url {
    position: absolute; left: 0; right: 0; top: 250px; text-align: center;
    color: var(--on-blue); font-size: 30px; letter-spacing: .5px;
  }
  .back-offer {
    position: absolute; left: 0; right: 0; top: 305px; text-align: center;
    color: var(--on-blue); font-size: 18px; letter-spacing: 1px;
  }

  /* front side */
  .front-wave { position: absolute; inset: 0; }
  .front-brand {
    position: absolute; left: 50px; top: 140px;
    display: flex; align-items: center; gap: 16px;
  }
  .front-brand__dot { width: 96px; height: 96px; border-radius: 50%; background: var(--mark-teal); }
  .front-brand__name { color: var(--ink); font-weight: 700; font-size: 30px; }
  .holder {
    position: absolute; right: 40px; top: 22px; text-align: right;
    color: var(--ink); font-size: 27px; line-height: 1.25;
  }
  .contact-list {
    position: absolute; right: 30px; top: 168px; list-style: none;
  }
  .contact-list__item {
    display: flex; align-items: center; justify-content: flex-end; gap: 12px;
    height: 42px; color: var(--on-blue); font-size: 18px;
  }
  .contact-list__icon { width: 24px; height: 24px; flex: none; }
</style>
</head>
<body>
<main class="sheet">

  <section class="card card--back" aria-label="Card back">
    <div class="back-brand">
      <span class="back-brand__dot"></span>
      <span class="back-brand__name">Tin Lantern</span>
    </div>
    <p class="back-url">www.tinlantern-example.com</p>
    <p class="back-offer">Custom designs available</p>
  </section>

  <section class="card card--front" aria-label="Card front">
    <svg class="front-wave" width="700" height="400" viewBox="0 0 700 400" aria-hidden="true">
      <path fill="var(--brand-blue)" d="M0,330 C200,360 330,300 430,200 C520,110 600,92 700,96 L700,400 L0,400 Z"/>
      <path fill="none" stroke="var(--accent-sky)" stroke-width="6" stroke-linecap="round"
            d="M60,378 C240,360 355,295 455,200 C540,128 618,112 690,112"/>
    </svg>

    <div class="front-brand">
      <span class="front-brand__dot"></span>
      <span class="front-brand__name">Tin Lantern</span>
    </div>

    <div class="holder">
      <p class="holder__name">Name</p>
      <p class="holder__role">designation</p>
    </div>

    <ul class="contact-list">
      <li class="contact-list__item">Address
        <svg class="contact-list__icon" viewBox="0 0 24 24"><path fill="#fff" d="M12 2a7 7 0 0 0-7 7c0 5 7 13 7 13s7-8 7-13a7 7 0 0 0-7-7zm0 9.5A2.5 2.5 0 1 1 12 6.5a2.5 2.5 0 0 1 0 5z"/></svg>
      </li>
      <li class="contact-list__item">Mobile, Phone
        <svg class="contact-list__icon" viewBox="0 0 24 24"><path fill="#fff" d="M6.6 10.8a15 15 0 0 0 6.6 6.6l2.2-2.2a1 1 0 0 1 1-.25 11 11 0 0 0 3.6.6 1 1 0 0 1 1 1V20a1 1 0 0 1-1 1A17 17 0 0 1 3 4a1 1 0 0 1 1-1h3.5a1 1 0 0 1 1 1 11 11 0 0 0 .6 3.6 1 1 0 0 1-.25 1z"/></svg>
      </li>
      <li class="contact-list__item">Fax
        <svg class="contact-list__icon" viewBox="0 0 24 24"><path fill="#fff" d="M7 3h10v5H7zM4 9h16a2 2 0 0 1 2 2v6h-4v4H6v-4H2v-6a2 2 0 0 1 2-2zm4 7v3h8v-3z"/></svg>
      </li>
      <li class="contact-list__item">email
        <svg class="contact-list__icon" viewBox="0 0 24 24"><rect x="2" y="5" width="20" height="14" fill="#fff"/><path d="M2 5l10 8 10-8" fill="none" stroke="var(--brand-blue)" stroke-width="1.6"/></svg>
      </li>
      <li class="contact-list__item">website
        <svg class="contact-list__icon" viewBox="0 0 24 24" fill="none" stroke="#fff" stroke-width="1.6"><circle cx="12" cy="12" r="10"/><ellipse cx="12" cy="12" rx="4.5" ry="10"/><path d="M2 12h20M4 7h16M4 17h16"/></svg>
      </li>
    </ul>
  </section>

</main>
</body>
</html>
```